Bodywork Quietude Business Card Design

I want to create a very elegant and sophisticated two sided business card for my massage practice (www.bodyworkquietude.net). I have attached the logo and a PDF with some ideas down for the back of the card but I am open to suggestions. I will want to tie in a post card and flyer to the card later.
Similar colors to website would be great.
Target Market(s)
High end clientele, people looking for a sophisticated spa experience.
Industry/Entity Type
Massage
Contact Information for Business Card
Bodywork Quietude
7318 Larkspur Ave S, Suite 305
Seattle, WA 98103
(206) 555-0147
www.bodyworkquietude.net
Look and feel

```html
<!DOCTYPE html>
<html lang="en">
<head>
<meta charset="utf-8">
<title>Bodywork Quietude — Business Card</title>
<link href="https://fonts.googleapis.com/css2?family=Tinos:wght@400;700&display=swap" rel="stylesheet">
<style>
  :root {
    --backdrop: #c6c5c6;
    --card-front: #1c3a4a;
    --card-back: #1d3443;
    --ink-cream: #ede4d6;
    --motif: #24404f;
  }
  * { margin: 0; padding: 0; box-sizing: border-box; }
  html, body { width: 1199px; height: 1200px; overflow: hidden; }
  body {
    background: var(--backdrop);
    font-family: "Tinos", "Times New Roman", serif;
    color: var(--ink-cream);
    position: relative;
  }
  .card {
    position: absolute;
    width: 597px;
    height: 341px;
    overflow: hidden;
  }
  .card--front { left: 298px; top: 191px; background: var(--card-front); }
  .card--back { left: 303px; top: 623px; background: var(--card-back); }

  .brand-name {
    position: absolute;
    font-weight: 400;
    letter-spacing: 0.5px;
    text-transform: uppercase;
    white-space: nowrap;
    color: var(--ink-cream);
  }
  .card--front .brand-name {
    left: 0; right: 0; top: 92px;
    text-align: center;
    font-size: 25px;
  }
  .card--front .brand-mark {
    position: absolute;
    left: 50%; top: 62px;
    width: 14px; height: 14px;
    margin-left: -7px;
    border-radius: 50%;
    background: var(--ink-cream);
  }
  .service-list {
    position: absolute;
    left: 0; right: 0; top: 218px;
    list-style: none;
    text-align: center;
    font-weight: 700;
    font-size: 13.5px;
    line-height: 17.3px;
  }
  .house-calls {
    position: absolute;
    left: 0; right: 0; top: 292px;
    text-align: center;
    font-weight: 700;
    font-size: 13.5px;
  }

  .back-motif {
    position: absolute;
    right: 0; top: 0;
    width: 240px; height: 341px;
    background: radial-gradient(ellipse at 80% 50%, var(--motif) 0%, rgba(36,64,79,0.4) 55%, rgba(29,52,67,0) 80%);
  }
  .card--back .brand-name {
    left: 38px; top: 72px;
    font-size: 17px;
  }
  .card--back .brand-mark {
    position: absolute;
    left: 110px; top: 48px;
    width: 12px; height: 12px;
    border-radius: 50%;
    background: var(--ink-cream);
  }
  .back-service {
    position: absolute;
    left: 38px; top: 162px;
    font-weight: 700;
    font-size: 13.5px;
  }
  .divider {
    position: absolute;
    left: 35px; top: 207px;
    width: 519px; height: 1px;
    background: var(--ink-cream);
  }
  .contact-list {
    position: absolute;
    left: 38px; top: 230px;
    list-style: none;
    font-weight: 700;
    font-size: 13.5px;
  }
  .contact-list li {
    display: flex;
    align-items: center;
    height: 28.5px;
  }
  .contact-list svg {
    width: 15px; height: 15px;
    margin-right: 13px;
    fill: var(--ink-cream);
    flex: none;
  }
</style>
</head>
<body>
  <section class="card card--front" aria-label="Business card front">
    <span class="brand-mark"></span>
    <div class="brand-name">Bodywork Quietude</div>
    <ul class="service-list">
      <li>Deep Lomi Ultra Relaxtion Massage</li>
      <li>Nurturing Touch Massage</li>
      <li>Thai Yoga Massage</li>
    </ul>
    <p class="house-calls">We Make House Calls</p>
  </section>

  <section class="card card--back" aria-label="Business card back">
    <div class="back-motif" role="img" aria-label="Faint large floral petal motif in deep teal"></div>
    <span class="brand-mark"></span>
    <div class="brand-name">Bodywork Quietude</div>
    <p class="back-service">Deep Lomi Ultra Relaxation Massage</p>
    <div class="divider"></div>
    <ul class="contact-list">
      <li>
        <svg viewBox="0 0 24 24" aria-hidden="true"><path d="M6.6 10.8a15.2 15.2 0 0 0 6.6 6.6l2.2-2.2a1 1 0 0 1 1-.25 11.4 11.4 0 0 0 3.6.57 1 1 0 0 1 1 1V20a1 1 0 0 1-1 1A17 17 0 0 1 3 4a1 1 0 0 1 1-1h3.5a1 1 0 0 1 1 1c0 1.25.2 2.45.57 3.57a1 1 0 0 1-.25 1z"/></svg>
        (206) 555-0147
      </li>
      <li>
        <svg viewBox="0 0 24 24" aria-hidden="true"><path d="M12 2a7 7 0 0 0-7 7c0 5.25 7 13 7 13s7-7.75 7-13a7 7 0 0 0-7-7zm0 9.5A2.5 2.5 0 1 1 12 6.5a2.5 2.5 0 0 1 0 5z"/></svg>
        7318 Larkspur Ave S, Suite 305 Seattle, WA 98103
      </li>
      <li>
        <svg viewBox="0 0 24 24" aria-hidden="true"><path d="M12 2a10 10 0 1 0 0 20 10 10 0 0 0 0-20zm6.9 6h-2.9a15 15 0 0 0-1.4-3.6A8 8 0 0 1 18.9 8zM12 4c.8 1.2 1.5 2.5 1.9 4h-3.8c.4-1.5 1.1-2.8 1.9-4zM4.3 14a8 8 0 0 1 0-4h3.4a16 16 0 0 0 0 4zm.8 2h2.9a15 15 0 0 0 1.4 3.6A8 8 0 0 1 5.1 16zM8 8H5.1a8 8 0 0 1 4.3-3.6A15 15 0 0 0 8 8zm4 12c-.8-1.2-1.5-2.5-1.9-4h3.8c-.4 1.5-1.1 2.8-1.9 4zm2.3-6H9.7a14 14 0 0 1 0-4h4.6a14 14 0 0 1 0 4zm.3 5.6A15 15 0 0 0 16 16h2.9a8 8 0 0 1-4.3 3.6zm1.7-5.6a16 16 0 0 0 0-4h3.4a8 8 0 0 1 0 4z"/></svg>
        www.bodyworkquietude.net
      </li>
    </ul>
  </section>
</body>
</html>
```